Bref créative
QDRL Stationary
Professional
Delvonte Ashby
CEO
4815 Marigold Ln
Killeen, TX 76549
dashby@qdrlinc.example
www.QDRLInc.example
My company Logo should be placed on the back of the card.

```html
<!DOCTYPE html>
<html lang="en">
<head>
<meta charset="UTF-8">
<title>QDRL Business Card</title>
<link rel="stylesheet" href="https://fonts.googleapis.com/css2?family=Arimo:wght@400;700&display=swap">
<style>
  :root {
    --backdrop: #ecebe8;
    --card: #ffffff;
    --ink: #1a1a1a;
    --brand-green: #2f8a12;
    --icon-green: #3e9a1c;
  }
  * { margin: 0; padding: 0; box-sizing: border-box; }
  html, body {
    width: 1200px;
    height: 780px;
    overflow: hidden;
    background: var(--backdrop);
    font-family: "Arimo", Arial, sans-serif;
    color: var(--ink);
  }
  .card {
    position: absolute;
    left: 75px;
    top: 90px;
    width: 1050px;
    height: 600px;
    background: var(--card);
    border-radius: 36px;
    box-shadow: 0 10px 30px rgba(0,0,0,0.12);
  }
  .brand {
    position: absolute;
    left: 78px;
    top: 200px;
    display: flex;
    align-items: center;
    gap: 22px;
  }
  .brand-dot {
    width: 58px;
    height: 58px;
    border-radius: 50%;
    background: var(--brand-green);
  }
  .brand-name {
    font-weight: 700;
    font-size: 92px;
    letter-spacing: 2px;
    line-height: 1;
    color: var(--ink);
  }
  .person {
    position: absolute;
    right: 78px;
    top: 292px;
    text-align: right;
  }
  .person-name {
    font-weight: 700;
    font-size: 34px;
    color: var(--brand-green);
  }
  .person-title {
    font-size: 24px;
    margin-top: 6px;
  }
  .address {
    position: absolute;
    left: 78px;
    top: 410px;
    font-size: 24px;
  }
  .contacts {
    position: absolute;
    left: 78px;
    top: 458px;
    display: grid;
    grid-template-columns: auto auto;
    column-gap: 30px;
    row-gap: 14px;
    font-size: 24px;
  }
  .contact {
    display: flex;
    align-items: center;
    gap: 10px;
  }
  .contact svg { width: 26px; height: 26px; fill: var(--icon-green); flex: none; }
  .at-sign {
    font-weight: 700;
    font-size: 30px;
    color: var(--icon-green);
    line-height: 1;
  }
</style>
</head>
<body>
  <main class="card">
    <div class="brand">
      <span class="brand-dot"></span>
      <span class="brand-name">QDRL</span>
    </div>

    <div class="person">
      <div class="person-name">Delvonte Ashby</div>
      <div class="person-title">CEO</div>
    </div>

    <p class="address">4815 Marigold Ln, Killeen, TX 76549</p>

    <div class="contacts">
      <div class="contact">
        <svg viewBox="0 0 24 24" aria-hidden="true"><path d="M6.6 10.8c1.4 2.8 3.8 5.1 6.6 6.6l2.2-2.2c.3-.3.7-.4 1-.2 1.1.4 2.3.6 3.6.6.6 0 1 .4 1 1V20c0 .6-.4 1-1 1C10.6 21 3 13.4 3 4c0-.6.4-1 1-1h3.5c.6 0 1 .4 1 1 0 1.3.2 2.5.6 3.6.1.3 0 .7-.2 1z"/></svg>
        <span>(T) 866-555-0142</span>
      </div>
      <div class="contact">
        <svg viewBox="0 0 24 24" aria-hidden="true"><path d="M8 1h8c1.1 0 2 .9 2 2v18c0 1.1-.9 2-2 2H8c-1.1 0-2-.9-2-2V3c0-1.1.9-2 2-2zm0 3v13h8V4H8zm4 15a1.2 1.2 0 100 2.4 1.2 1.2 0 000-2.4z"/></svg>
        <span>254-555-0187</span>
      </div>
      <div class="contact">
        <svg viewBox="0 0 24 24" aria-hidden="true"><path d="M7 2h8l3 3v4H7V2zm-3 8h16c1.1 0 2 .9 2 2v7c0 1.1-.9 2-2 2H4c-1.1 0-2-.9-2-2v-7c0-1.1.9-2 2-2zm3 4v2h3v-2H7zm5 0v2h3v-2h-3z"/></svg>
        <span>866-555-0142</span>
      </div>
      <div class="contact">
        <span class="at-sign" aria-hidden="true">@</span>
        <span>dashby@qdrlinc.example</span>
      </div>
    </div>
  </main>
</body>
</html>
```